Bright Haven Estate Sales web design

We are looking to launch an Estate Sales Website for Nashville, TN. The name of our Business is Bright Haven Estate Sales. We would like to give you a blank slate so that you can showcase your design skills for us. The few things we are looking for are a nice header graphic of a house or a stock image of an estate sale. Near the header graphic we would like a quick inquiry form. If not on the right side of the header maybe midway down the site. We potentially want to see what purple and Gold look like on the site however this is not a must. We have over 20 years of industry related experience.

1. Buttons at top of the website will be.
a. Services
b. Upcoming Sales
c. About Us
d. FAQs
e. Resources

Services we offer:
1. Estate Sales
2. Cleanouts
3. Appraisals

Sites We like:
https://www.corvellestatesales.example/

We don't have a logo yet so if you have ideas please share them with us. Below are 2 ideas however if you have your own thoughts please ignore.

1. Oval ornate frame, gold and black, with BHES in the middle, deep purple. Think of catering to high class people..font should be fancy as opposed to simple.

2. Another option, Bright Haven in bold fancy script, same colors, with Estate Sales below, small different font, black.

```html
<!DOCTYPE html>
<html lang="en">
<head>
<meta charset="utf-8">
<title>Bright Haven Estate Sales</title>
<link rel="stylesheet" href="https://fonts.googleapis.com/css2?family=Lexend:wght@300;400;500;600;700&family=Montserrat:wght@400;500;600;700&family=Great+Vibes&display=swap">
<style>
:root{
  --purple:#4b2384;
  --purple-deep:#3a176d;
  --purple-dark:#2d0f5a;
  --gold:#e2b623;
  --gold-light:#f5d640;
  --gold-deep:#c59614;
  --ink:#2a1a4a;
  --muted:#5a5368;
  --white:#ffffff;
  --line:#e8d27a;
}
*{box-sizing:border-box;margin:0;padding:0}
html,body{width:1200px;height:4612px;overflow:hidden}
body{position:relative;background:var(--white);font-family:"Montserrat",sans-serif;color:var(--ink)}
.abs{position:absolute}
.display{font-family:"Lexend",sans-serif}
.gold-grad{background:linear-gradient(135deg,var(--gold-light),var(--gold) 55%,var(--gold-deep))}
.field{position:absolute;background:#fff;font-size:11px;color:#333;padding:0 16px;display:flex;align-items:center}
.field.area{align-items:flex-start;padding-top:16px}
.btn-purple{background:var(--purple);color:#fff;font-family:"Lexend",sans-serif;font-weight:600;display:flex;align-items:center;justify-content:center}
.btn-gold{color:var(--ink);font-family:"Lexend",sans-serif;font-weight:600;display:flex;align-items:center;justify-content:center}
.eyebrow{font-family:"Lexend",sans-serif;letter-spacing:2px;color:var(--gold-deep);font-size:17px;font-weight:400}
.h2{font-family:"Lexend",sans-serif;font-size:40px;font-weight:400;color:var(--purple)}
.h2 b{font-weight:700}
.rule{position:absolute;height:2px;background:var(--gold)}
.rule i{position:absolute;top:-3px;width:8px;height:8px;border-radius:50%;background:var(--gold)}

/* header */
.site-header{position:absolute;left:0;top:0;width:1200px;height:80px;z-index:3}
.brand{position:absolute;left:118px;top:10px;color:#fff;font-family:"Lexend",sans-serif}
.brand .name{font-size:30px;font-weight:600;line-height:1}
.brand .sub{font-size:16px;font-weight:400;margin-top:4px}
.nav a{position:absolute;top:31px;color:#fff;font-size:14px;font-weight:500;text-decoration:none}
.quote{position:absolute;left:968px;top:23px;width:130px;height:37px;font-size:13px}

/* hero */
.hero{position:absolute;left:0;top:0;width:1200px;height:690px;background:linear-gradient(180deg,#4a2386 0%,#6b3d86 30%,#b6704a 60%,#5a3a2a 85%,#2f2a1f 100%)}
.hero-frame{position:absolute;left:233px;top:152px;width:730px;height:113px;border:2px solid var(--gold)}
.hero-title{position:absolute;left:0;top:116px;width:1200px;text-align:center;font-family:"Lexend",sans-serif;font-size:60px;font-weight:500;color:#fff}
.hero-title span{background:transparent;padding:0 12px;position:relative}
.hero-sub{position:absolute;left:0;top:196px;width:1200px;text-align:center;font-size:22px;color:#fff}
.hero-btn{position:absolute;left:478px;top:243px;width:252px;height:47px;font-size:15px}

/* enquiry */
.enquiry-outline{position:absolute;left:122px;top:602px;width:975px;height:160px;border:2px solid var(--gold)}
.enquiry{position:absolute;left:132px;top:590px;width:963px;height:160px}
.enquiry-title{position:absolute;left:178px;top:628px;font-family:"Great Vibes",cursive;font-size:48px;color:#fff}

/* about */
.about-back{position:absolute;left:124px;top:833px;width:476px;height:412px;background:var(--purple)}
.about-corner{position:absolute;left:124px;top:1090px;width:200px;height:160px}
.about-photo{position:absolute;left:137px;top:848px;width:461px;height:390px;background:linear-gradient(180deg,#8fa8c9 0%,#d9b58a 45%,#8a6a4a 70%,#4e6a35 100%)}
.badge{position:absolute;left:500px;top:1155px;width:125px;height:115px;text-align:center;color:var(--ink)}
.badge .num{font-family:"Lexend",sans-serif;font-size:60px;line-height:1;margin-top:4px}
.badge .txt{font-size:13px;line-height:1.15;margin-top:4px}
.about-copy{position:absolute;left:665px;top:970px;width:450px;font-size:15.5px;line-height:26px;color:#3c3450}
.about-copy p+p{margin-top:16px}

/* services */
.services-band{position:absolute;left:0;top:1300px;width:1200px;height:512px}
.svc{position:absolute;top:1605px;width:310px;height:277px;background:#fff;border:2px solid var(--line);text-align:center}
.svc.active{background:var(--purple);border-color:var(--purple);color:#fff}
.svc-icon{position:absolute;top:-44px;left:105px;width:100px;height:100px;border-radius:50%;display:flex;align-items:center;justify-content:center}
.svc.active .svc-icon{background:var(--purple);border:3px solid #fff}
.svc h3{font-family:"Lexend",sans-serif;font-weight:500;font-size:24px;margin-top:75px;color:var(--purple)}
.svc.active h3{color:#fff}
.svc p{font-size:12.5px;line-height:21px;margin:14px 26px 0;color:#5a3f8a}
.svc.active p{color:#fff}
.svc .more{position:absolute;left:91px;top:205px;width:128px;height:42px;border:2px solid var(--gold);font-size:12.5px;font-weight:600;display:flex;align-items:center;justify-content:center;color:var(--purple)}
.svc.active .more{border-color:#fff;color:#fff}

/* sales */
.sale{position:absolute;top:2066px;width:266px;height:334px;border:2px solid var(--line);background:#fff}
.sale .img{height:197px}
.sale .date{position:absolute;left:28px;top:184px;width:94px;height:26px;font-size:12px;font-weight:600;color:var(--ink)}
.sale h4{position:absolute;left:28px;top:226px;font-size:14px;font-weight:700;color:var(--purple)}
.sale p{position:absolute;left:28px;top:248px;font-size:11px;line-height:13px;color:#666;width:210px}
.sale .loc{position:absolute;left:28px;top:289px;font-size:11px;color:var(--purple);display:flex;gap:5px;align-items:center}
.dots span{position:absolute;top:2433px;height:3px;width:46px;background:#c9c3d8}

/* process */
.process{position:absolute;left:0;top:2488px;width:1200px;height:682px;background:linear-gradient(90deg,var(--purple-deep) 0%,var(--purple) 55%,#4e2a86 100%)}
.process-photo{position:absolute;left:700px;top:2540px;width:500px;height:590px;background:linear-gradient(200deg,#b9c2dd 0%,#8a84b8 35%,#e0b46a 60%,#3b2f5a 85%,#2f2748 100%);-webkit-mask-image:linear-gradient(90deg,transparent,#000 30%);mask-image:linear-gradient(90deg,transparent,#000 30%)}
.step{position:absolute;left:130px;color:#fff}
.step .n{position:absolute;left:0;top:-6px;font-family:"Lexend",sans-serif;font-size:48px;font-weight:300;color:transparent;-webkit-text-stroke:1.5px var(--gold)}
.step .d{position:absolute;left:43px;top:14px;width:12px;height:12px;border-radius:50%;border:2px solid var(--gold)}
.step h4{position:absolute;left:81px;top:0;font-family:"Lexend",sans-serif;font-size:19px;font-weight:600;white-space:nowrap}
.step p{position:absolute;left:81px;top:28px;width:330px;font-size:12.5px;line-height:19px;color:#e5dcf3}
.step-line{position:absolute;left:179px;top:2690px;width:0;height:290px;border-left:2px dotted var(--gold)}

/* contact */
.contact{position:absolute;left:142px;top:3080px;width:909px;height:488px}

/* blogs */
.blog-big{position:absolute;left:130px;top:3720px;width:492px;height:385px;background:linear-gradient(180deg,#e9e9ea 0%,#c9c9cb 55%,#5d5d62 100%)}
.blog-big .meta{position:absolute;left:34px;top:290px;width:110px;height:22px;background:var(--purple);color:#fff;font-size:11px;display:flex;align-items:center;justify-content:center;gap:5px}
.blog-big h3{position:absolute;left:34px;top:322px;width:420px;color:#fff;font-family:"Lexend",sans-serif;font-weight:500;font-size:19px;line-height:25px}
.blog-sm{position:absolute;left:634px;width:452px;height:187px;border:2px solid #e0d7ee;background:#fff}
.blog-sm .img{position:absolute;left:0;top:0;width:219px;height:183px}
.blog-sm .meta{position:absolute;left:242px;top:22px;width:100px;height:21px;background:var(--purple);color:#fff;font-size:10px;display:flex;align-items:center;justify-content:center;gap:4px}
.blog-sm h4{position:absolute;left:242px;top:58px;font-size:13.5px;font-weight:700;color:var(--purple)}
.blog-sm p{position:absolute;left:242px;top:80px;width:195px;font-size:10.5px;line-height:15px;color:#666}
.blog-sm .lm{position:absolute;left:242px;top:142px;width:100px;height:24px;border:1.5px solid var(--gold);font-size:9px;font-weight:600;color:var(--gold-deep);display:flex;align-items:center;justify-content:center;letter-spacing:1px}

/* footer */
.site-footer{position:absolute;left:0;top:4193px;width:1200px;height:419px;background:linear-gradient(180deg,var(--purple) 0%,var(--purple-deep) 100%);color:#fff}
.f-brand{position:absolute;left:133px;top:82px;font-family:"Lexend",sans-serif}
.f-brand .name{font-size:36px;font-weight:600;line-height:1}
.f-brand .sub{font-size:19px;margin-top:6px}
.social span{position:absolute;top:178px;width:28px;height:28px;border-radius:50%;background:var(--gold)}
.f-col{position:absolute;top:88px}
.f-col h5{font-family:"Lexend",sans-serif;font-size:15px;font-weight:600;letter-spacing:.5px}
.f-col ul{list-style:none;margin-top:10px}
.f-col li{font-size:12.5px;line-height:29px;color:#e6defa}
.f-div{position:absolute;top:82px;width:2px;height:150px;background:var(--gold)}
.f-contact li{display:flex;align-items:center;gap:12px;line-height:40px}
.f-contact .ic{width:22px;height:22px;border-radius:50%;background:var(--gold);display:flex;align-items:center;justify-content:center}
.f-bottom{position:absolute;left:0;top:342px;width:1200px;border-top:1px solid rgba(255,255,255,.25)}
.f-copy{position:absolute;left:0;top:370px;width:1200px;text-align:center;font-size:11.5px;color:#bfb2db}
</style>
</head>
<body>

<!-- hero -->
<section class="hero" role="img" aria-label="Large modern farmhouse at sunset with lit windows and trees"></section>
<header class="site-header">
  <div class="brand"><div class="name">Bright Haven</div><div class="sub">Estate Sales</div></div>
  <nav class="nav">
    <a style="left:344px">Services &#8964;</a>
    <a style="left:463px">Upcoming Sales</a>
    <a style="left:641px">About Us</a>
    <a style="left:764px">FAQs</a>
    <a style="left:859px">Resources</a>
  </nav>
  <div class="quote btn-gold gold-grad">Get a Quote</div>
</header>
<div class="hero-frame"></div>
<h1 class="hero-title"><span>Bright Haven Estate Sales</span></h1>
<p class="hero-sub">The most trusted estate sale team in the industry.</p>
<div class="hero-btn btn-gold gold-grad">Schedule a Consultation</div>

<!-- enquiry -->
<div class="enquiry-outline"></div>
<form class="enquiry gold-grad"></form>
<div class="enquiry-title">Enquiry now</div>
<div class="field" style="left:393px;top:630px;width:217px;height:37px">First Name*</div>
<div class="field" style="left:617px;top:630px;width:216px;height:37px">Last Name*</div>
<div class="field" style="left:840px;top:630px;width:217px;height:37px">City</div>
<div class="field" style="left:393px;top:676px;width:217px;height:37px">Email address*</div>
<div class="field" style="left:617px;top:676px;width:216px;height:37px">Phone*</div>
<div class="btn-purple abs" style="left:840px;top:676px;width:217px;height:37px;font-size:13px">Submit Now</div>

<!-- about -->
<div class="about-back"></div>
<div class="about-corner gold-grad"></div>
<div class="about-photo" role="img" aria-label="Two-storey house with white picket fence at dusk"></div>
<div class="badge gold-grad"><div class="num">20</div><div class="txt">YEARS OF<br>EXPERIENCE</div></div>
<div class="eyebrow abs" style="left:662px;top:878px">OUR STORY</div>
<h2 class="h2 abs" style="left:664px;top:900px;font-size:38px"><b>Bright Haven</b> Estate Sales</h2>
<div class="rule" style="left:1095px;top:922px;width:105px"><i style="left:0"></i></div>
<div class="about-copy">
  <p>Lorem ipsum dolor sit amet, consectetur adipiscing elit, sed do eiusmod tempor incididunt ut labore et dolore magna aliqua. Quis ipsum suspendisse ultrices gravida. Risus commodo viverra maecenas accumsan</p>
  <p>Aacus vel facilisis. Lorem ipsum dolor sit amet, consectetur adipiscing elit, sed do eiusmod tempor incididunt ut labore et dolore magna aliqua. Quis ipsum</p>
</div>
<div class="btn-purple abs" style="left:666px;top:1188px;width:175px;height:53px;font-size:16px">Learn More</div>

<!-- services -->
<svg class="services-band" width="1200" height="512" viewBox="0 0 1200 512" role="img" aria-label="Gold city skyline backdrop">
  <defs>
    <linearGradient id="sg" x1="0" y1="0" x2="1" y2="1">
      <stop offset="0" stop-color="#e0b320"/><stop offset=".5" stop-color="#f5d83e"/><stop offset="1" stop-color="#d9a918"/>
    </linearGradient>
  </defs>
  <rect width="1200" height="512" fill="url(#sg)"/>
  <path d="M0 0 L1200 0 L1200 18 L600 112 L0 20 Z" fill="#fff"/>
  <path d="M0 0 L600 100 L1200 2" fill="none" stroke="#4b2384" stroke-width="10"/>
</svg>
<div class="eyebrow abs" style="left:0;top:1452px;width:1200px;text-align:center;color:var(--ink);font-size:16px">WHAT WE DO</div>
<h2 class="h2 abs" style="left:0;top:1472px;width:1200px;text-align:center;color:var(--ink)">Services <b style="color:var(--purple)">Provide</b></h2>

<div class="svc" style="left:115px">
  <div class="svc-icon gold-grad"><svg width="46" height="40" viewBox="0 0 46 40" fill="none" stroke="#3a176d" stroke-width="2"><rect x="14" y="4" width="18" height="34"/><rect x="4" y="18" width="10" height="20"/><rect x="32" y="18" width="10" height="20"/><path d="M19 10h3M24 10h3M19 17h3M24 17h3M19 24h3M24 24h3M20 38v-7h6v7"/></svg></div>
  <h3>Estate Sales</h3>
  <p>Lorem ipsum dolor sit amet, consectetur adipiscing elit, sed do eiusmod tempor incididunt ut labo</p>
  <div class="more">Learn More</div>
</div>
<div class="svc active" style="left:446px">
  <div class="svc-icon"><svg width="46" height="40" viewBox="0 0 46 40" fill="none" stroke="#fff" stroke-width="2"><path d="M4 20 L23 4 L42 20"/><path d="M9 16v22h28V16"/><rect x="18" y="24" width="10" height="14"/><path d="M32 8v6M29 11h6M10 6v4M8 8h4"/></svg></div>
  <h3>Cleanouts</h3>
  <p>Lorem ipsum dolor sit amet, consectetur adipiscing elit sed do eiusmod tempor incididunt ut labo</p>
  <div class="more">Learn More</div>
</div>
<div class="svc" style="left:775px">
  <div class="svc-icon gold-grad"><svg width="46" height="40" viewBox="0 0 46 40" fill="none" stroke="#3a176d" stroke-width="2"><path d="M4 20 L23 4 L42 20"/><path d="M9 16v22h28V16"/><circle cx="22" cy="25" r="6"/><path d="M26 29l5 5"/></svg></div>
  <h3>Appraisals</h3>
  <p>Lorem ipsum dolor sit amet, consectetur adipiscing elit, sed do eiusmod tempor incididunt ut labo</p>
  <div class="more">Learn More</div>
</div>

<!-- upcoming sales -->
<div class="eyebrow abs" style="left:107px;top:1962px">OUR STORY</div>
<h2 class="h2 abs" style="left:106px;top:1984px">Upcoming <b>Sales</b></h2>
<div class="rule" style="left:0;top:2010px;width:86px"><i style="right:0"></i></div>

<article class="sale" style="left:115px"><div class="img" role="img" aria-label="Suburban two-storey house with garage" style="background:linear-gradient(180deg,#a9c4e3,#7a8aa0 55%,#5d7a3e)"></div><div class="date gold-grad abs" style="display:flex;align-items:center;justify-content:center">01 MAR 2024</div><h4>Lorem ipsum dolor sit</h4><p>amet consectetur adipiscing elit, sed do eiusmod tempor</p><div class="loc"><svg width="10" height="13" viewBox="0 0 10 13"><path d="M5 0a5 5 0 0 0-5 5c0 4 5 8 5 8s5-4 5-8a5 5 0 0 0-5-5z" fill="#4b2384"/><circle cx="5" cy="5" r="1.8" fill="#fff"/></svg>Location</div></article>
<article class="sale" style="left:398px"><div class="img" role="img" aria-label="Modern house with dark siding and wood accents" style="background:linear-gradient(180deg,#c9cfd6,#4a4a48 55%,#5c6a3a)"></div><div class="date gold-grad abs" style="display:flex;align-items:center;justify-content:center">05 MAR 2024</div><h4>Lorem ipsum dolor sit</h4><p>amet consectetur adipiscing elit, sed do eiusmod tempor</p><div class="loc"><svg width="10" height="13" viewBox="0 0 10 13"><path d="M5 0a5 5 0 0 0-5 5c0 4 5 8 5 8s5-4 5-8a5 5 0 0 0-5-5z" fill="#4b2384"/><circle cx="5" cy="5" r="1.8" fill="#fff"/></svg>Location</div></article>
<article class="sale" style="left:681px"><div class="img" role="img" aria-label="Craftsman house with green lawn under blue sky" style="background:linear-gradient(180deg,#6fa0e0,#9fb7c9 45%,#6b6a5a 65%,#4e8a2e)"></div><div class="date gold-grad abs" style="display:flex;align-items:center;justify-content:center">15 MAR 2024</div><h4>Lorem ipsum dolor sit</h4><p>amet consectetur adipiscing elit, sed do eiusmod tempor</p><div class="loc"><svg width="10" height="13" viewBox="0 0 10 13"><path d="M5 0a5 5 0 0 0-5 5c0 4 5 8 5 8s5-4 5-8a5 5 0 0 0-5-5z" fill="#4b2384"/><circle cx="5" cy="5" r="1.8" fill="#fff"/></svg>Location</div></article>
<article class="sale" style="left:964px"><div class="img" role="img" aria-label="Contemporary house with large windows at dusk" style="background:linear-gradient(180deg,#d8d8dc,#6b5a4a 50%,#3a3430)"></div><div class="date gold-grad abs" style="display:flex;align-items:center;justify-content:center">19 MAR 2024</div><h4>Lorem ipsum dolor sit</h4><p>amet consectetur adipiscing elit, sed do eiusmod tempor</p><div class="loc"><svg width="10" height="13" viewBox="0 0 10 13"><path d="M5 0a5 5 0 0 0-5 5c0 4 5 8 5 8s5-4 5-8a5 5 0 0 0-5-5z" fill="#4b2384"/><circle cx="5" cy="5" r="1.8" fill="#fff"/></svg>Location</div></article>
<div class="dots"><span style="left:576px;background:var(--purple)"></span><span style="left:636px"></span><span style="left:694px"></span></div>

<!-- process -->
<section class="process"></section>
<div class="process-photo" role="img" aria-label="White house with lit porch and patio at twilight"></div>
<h2 class="h2 abs" style="left:132px;top:2572px;color:#fff"><b>Our Process</b></h2>
<div class="rule" style="left:0;top:2596px;width:100px"><i style="right:0"></i></div>
<div class="step-line"></div>
<div class="step" style="top:2654px"><span class="n">1</span><span class="d"></span><h4>Free Consultation</h4><p>We will come to you and work out what the best solution for your unique situation</p></div>
<div class="step" style="top:2749px"><span class="n">2</span><span class="d"></span><h4>Estate Sale Set Up</h4><p>We set up, stage, price, and advertise all items in the estate sale.</p></div>
<div class="step" style="top:2844px"><span class="n">3</span><span class="d"></span><h4>Sale Days</h4><p>We will come to you and work out what the best solution for your unique situation</p></div>
<div class="step" style="top:2936px"><span class="n">4</span><span class="d"></span><h4>Post–Sale</h4><p>After the sale, you will get the full breakdown of the sale totals and a list of all transactions.</p></div>

<!-- contact -->
<form class="contact gold-grad"></form>
<div class="eyebrow abs" style="left:142px;top:3126px;width:909px;text-align:center;color:#fff;font-size:17px">CONTACT US</div>
<h2 class="h2 abs" style="left:142px;top:3146px;width:909px;text-align:center;color:#fff;font-size:38px">Schedule a <b>Consultation</b></h2>
<div class="field" style="left:242px;top:3222px;width:346px;height:45px;font-size:12px">First Name*</div>
<div class="field" style="left:600px;top:3222px;width:350px;height:45px;font-size:12px">Last Name*</div>
<div class="field" style="left:242px;top:3284px;width:346px;height:45px;font-size:12px">Email address*</div>
<div class="field" style="left:600px;top:3284px;width:350px;height:45px;font-size:12px">Phone*</div>
<div class="field area" style="left:242px;top:3345px;width:708px;height:100px;font-size:12px">Leave Message</div>
<div class="btn-purple abs" style="left:494px;top:3462px;width:202px;height:48px;font-size:16px">Send Message</div>

<!-- blogs -->
<div class="eyebrow abs" style="left:128px;top:3624px">RESOURCES</div>
<h2 class="h2 abs" style="left:127px;top:3646px">Latest <b>Blogs</b></h2>
<div class="rule" style="left:0;top:3668px;width:110px"><i style="right:0"></i></div>
<article class="blog-big" role="img" aria-label="Bright living room with sofa and tall windows">
  <div class="meta"><svg width="10" height="10" viewBox="0 0 10 10" fill="none" stroke="#fff"><circle cx="5" cy="5" r="4"/><path d="M5 2.5V5h2"/></svg>19 JAN 2024</div>
  <h3>Lorem ipsum dolor sit amet consec tetur adipiscing elit sed do</h3>
</article>
<article class="blog-sm" style="top:3720px">
  <div class="img" role="img" aria-label="Family relaxing together on a sofa at home" style="background:linear-gradient(180deg,#d9cfc2,#8a7a6a 60%,#3e4a5a)"></div>
  <div class="meta"><svg width="9" height="9" viewBox="0 0 10 10" fill="none" stroke="#fff"><circle cx="5" cy="5" r="4"/><path d="M5 2.5V5h2"/></svg>19 JAN 2024</div>
  <h4>Lorem ipsum dolor sit</h4>
  <p>Lorem ipsum dolor sit amet consectetur adipiscing elit sed do eiusmod tempor incididunt ut labor</p>
  <div class="lm">LEARN MORE</div>
</article>
<article class="blog-sm" style="top:3918px">
  <div class="img" role="img" aria-label="Family walking toward a house on a green lawn" style="background:linear-gradient(180deg,#c7d8e8,#7a7a78 50%,#5e8a3a)"></div>
  <div class="meta"><svg width="9" height="9" viewBox="0 0 10 10" fill="none" stroke="#fff"><circle cx="5" cy="5" r="4"/><path d="M5 2.5V5h2"/></svg>19 JAN 2024</div>
  <h4>Lorem ipsum dolor sit</h4>
  <p>Lorem ipsum dolor sit amet consectetur adipiscing elit sed do eiusmod tempor incididunt ut labor</p>
  <div class="lm">LEARN MORE</div>
</article>

<!-- footer -->
<footer class="site-footer">
  <div class="f-brand"><div class="name">Bright Haven</div><div class="sub">Estate Sales</div></div>
  <div class="social"><span style="left:141px"></span><span style="left:190px"></span><span style="left:239px"></span></div>
  <div class="f-div" style="left:391px"></div>
  <div class="f-col" style="left:422px"><h5>NAVIGATION</h5><ul><li>Services</li><li>Upcoming Sales</li><li>About Us</li><li>FAQs</li><li>Resources</li></ul></div>
  <div class="f-div" style="left:620px"></div>
  <div class="f-col" style="left:648px"><h5>RESOURCES</h5><ul><li>FAQs</li><li>Testimonials</li><li>Career</li><li>Privacy Policy</li><li>Terms and Conditions</li></ul></div>
  <div class="f-div" style="left:853px"></div>
  <div class="f-col f-contact" style="left:882px"><h5>CONTACT US</h5><ul>
    <li><span class="ic"><svg width="10" height="13" viewBox="0 0 10 13"><path d="M5 0a5 5 0 0 0-5 5c0 4 5 8 5 8s5-4 5-8a5 5 0 0 0-5-5z" fill="#3a176d"/></svg></span>418 Corlan Ave, Nashville, TN 37000</li>
    <li><span class="ic"><svg width="11" height="11" viewBox="0 0 12 12"><path d="M2 1l3 1 1 3-2 1a7 7 0 0 0 3 3l1-2 3 1 1 3c-6 1-11-4-10-10z" fill="#3a176d"/></svg></span>Tel: 615-555-0142</li>
    <li><span class="ic"><svg width="12" height="9" viewBox="0 0 12 9" fill="none" stroke="#3a176d" stroke-width="1.5"><rect x="1" y="1" width="10" height="7"/><path d="M1 1l5 4 5-4"/></svg></span>info@brighthaven.example</li>
  </ul></div>
  <div class="f-bottom"></div>
  <div class="f-copy">© 2024 Bright Haven Estate Sales. All Rights Reserved</div>
</footer>

</body>
</html>
```